Modern and appealing business Wordpress site

I've been operating my consulting firm for 5 years and feel like it is time to really improve on my web presence as I'm starting to get more national attention. I had a logo made through this service a couple of years ago, and would like to get a website that matches the look of it. The website will be used to (1) advertise my services (2) provide a brief overview of our management philosophies, and (3) host a resource library database. I understand HTML, but am not as familiar with how to code Wordpress, so I need someone that can help upload themes.

The website can be found at www.trelmondgroup.com.

For design, I prefer round designs to square and want the color scheme to match the attached logo. I have included both the full logo and the abbreviated one.

I also have a new picture for CFO uploaded. I plan on getting a new one for the CEO in the coming weeks, so I would like someone that I could get to help make the modification at a later time.

The resource database will be put into a document library (probably Kiln7) once the final design is completed rather than having multiple pages with links...just so you know the final vision for the site.

Reach out if you have any questions.

Target Market(s)

Community Action Agencies, Nonprofit Organization Leaders

Industry/Entity Type

Consulting

Coding

Coded - Design and coding required

Font styles to use
Sans Serif

Requirements
Must have
• Must match the color scheme of the attached logo

```html
<!DOCTYPE html>
<html lang="en">
<head>
<meta charset="utf-8">
<title>Trelmond Group – Leading Organizations to Excellence</title>
<link rel="stylesheet" href="https://fonts.googleapis.com/css2?family=Montserrat:wght@600;700&family=Roboto:ital,wght@0,400;0,500;0,700;1,400&display=swap">
<style>
:root{
  --blue:#2fa4da;
  --blue-dark:#1f8fc7;
  --grey:#4f4f51;
  --grey-dark:#3f3f41;
  --ink:#3a3a3c;
  --text:#6d6d6d;
  --light:#eef3f6;
  --white:#ffffff;
}
*{margin:0;padding:0;box-sizing:border-box}
html,body{width:1200px;height:3882px;overflow:hidden;background:var(--white)}
body{font-family:"Roboto",Arial,sans-serif;color:var(--ink)}
.page{position:relative;width:1200px;height:3882px;overflow:hidden}
.abs{position:absolute}
.heading{font-family:"Montserrat",Arial,sans-serif;font-weight:700;text-transform:uppercase;letter-spacing:.5px}
.accent{color:var(--blue)}
.btn{position:absolute;display:flex;align-items:center;justify-content:center;background:var(--blue);color:var(--white);border-radius:40px;font-weight:700;font-size:14px;text-transform:uppercase;letter-spacing:.3px}

/* header */
.logo{left:143px;top:36px;display:flex;align-items:center;gap:12px}
.logo-dot{width:58px;height:58px;border-radius:50%;background:var(--blue)}
.logo-name{font-family:"Montserrat",sans-serif;font-weight:700;font-size:40px;color:var(--blue);letter-spacing:1px}
.nav{left:557px;top:52px;display:flex;gap:33px;font-size:14px;font-weight:500;color:var(--ink)}
.nav .active{color:var(--ink);position:relative}
.nav .active::after{content:"";position:absolute;left:0;right:0;bottom:-12px;height:3px;background:var(--blue)}

/* hero */
.hero-photo{left:0;top:0;width:1200px;height:760px;background:linear-gradient(180deg,#f4f7f9 0%,#dbe7ee 55%,#b8c8d2 100%)}
.hero-figure{left:760px;top:160px;width:330px;height:560px;border-radius:170px 170px 0 0;background:linear-gradient(180deg,#5a6872,#2c353c)}
.hero-city{left:0;top:500px;width:1200px;height:240px;background:linear-gradient(180deg,rgba(120,140,155,.35),rgba(80,95,110,.55))}
.hero-title{left:143px;top:246px;font-size:42px;line-height:52px;color:var(--ink)}
.hero-title span{display:block}
.dots-v{left:1131px;top:362px;display:flex;flex-direction:column;gap:13px}
.dots-v i{width:5px;height:5px;border-radius:50%;background:#9aa9b3}
.dots-v i.on{background:var(--blue)}

/* about */
.about-photo{left:163px;top:852px;width:392px;height:286px;border-radius:60% 40% 50% 50%/55% 55% 45% 45%;background:linear-gradient(120deg,var(--blue) 0%,#4a8fb5 55%,#9aa3a8 100%)}
.about-title{left:621px;top:820px;font-size:44px}
.about-text{left:621px;top:884px;width:434px;font-size:14.5px;line-height:28px;color:var(--text);text-align:justify}

/* services */
.card{position:absolute;top:1161px;height:561px;overflow:hidden;color:var(--white);display:flex;flex-direction:column;align-items:center;justify-content:center;text-align:center}
.card-left{left:0;width:381px;border-top-right-radius:260px;background:linear-gradient(160deg,#5ab7e3,var(--blue-dark))}
.card-mid{left:403px;width:395px;background:linear-gradient(180deg,#5c5c5e,#3a3a3c);clip-path:polygon(0 28%,100% 0,100% 100%,0 100%)}
.card-right{left:819px;width:381px;border-top-left-radius:260px;background:linear-gradient(200deg,#3c9fd3,#1d77a8)}
.card-wedge{left:403px;top:1191px;width:520px;height:170px;background:var(--grey-dark);clip-path:polygon(0 100%,100% 0,60% 100%)}
.card h3{font-family:"Roboto",sans-serif;font-weight:700;font-size:36px;line-height:44px;text-transform:uppercase}
.card-mid h3{font-size:24px;margin-top:120px}
.card-mid p{width:330px;font-size:12px;line-height:23px;margin-top:10px;color:#e6e6e6}
.card-mid .btn{position:static;width:150px;height:52px;margin-top:20px}
.arrows{left:562px;top:1704px;display:flex;gap:2px}
.arrows span{width:36px;height:36px;border-radius:50%;background:var(--white);border:2px solid #bdbdbd;display:flex;align-items:center;justify-content:center}

/* testimonials */
.testi-bg{left:0;top:1745px;width:1200px;height:520px;background:linear-gradient(180deg,#eef0f2 0%,#f6f6f7 70%,#ffffff 100%)}
.testi-title{left:0;width:1200px;top:1834px;text-align:center;font-size:44px}
.quote{left:570px;top:1932px}
.testi-text{left:270px;width:660px;top:2010px;text-align:center;font-style:italic;font-size:19px;line-height:31px;color:#555}
.testi-author{left:0;width:1200px;top:2162px;text-align:center;font-size:19px;color:var(--blue);font-weight:500}
.dots-h{left:575px;top:2216px;display:flex;gap:8px}
.dots-h i{width:7px;height:7px;border-radius:50%;background:#b9b9b9}
.dots-h i.on{background:var(--blue)}

/* mission */
.mission-blue{left:436px;top:2310px;width:760px;height:196px;background:var(--blue);border-radius:0 98px 98px 0}
.mission-grey{left:5px;top:2310px;width:460px;height:196px;background:var(--grey);border-radius:98px 120px 120px 98px;border-right:14px solid var(--white)}
.mission-title{left:95px;top:2382px;font-size:44px;color:var(--white)}
.mission-text{left:562px;top:2362px;width:500px;font-size:18px;line-height:29px;color:var(--white)}

/* team */
.member{position:absolute;top:2580px;width:420px;text-align:center}
.member-ring{position:relative;width:320px;height:320px;margin:0 auto}
.member-photo{position:absolute;left:20px;top:22px;width:285px;height:285px;border-radius:50%}
.member h4{margin-top:16px;font-size:19px;font-weight:500;text-transform:uppercase;color:var(--ink)}
.member .role{margin-top:6px;font-size:17px;color:var(--blue)}
.member p{margin:18px auto 0;width:330px;font-size:12.5px;line-height:24px;color:var(--text)}
.member .btn{position:relative;margin:30px auto 0;width:152px;height:54px}

/* contact */
.contact-title{left:0;width:1200px;top:3424px;text-align:center;font-size:44px;color:var(--white)}
.label{font-size:15px;font-weight:500;color:var(--white)}
.field{position:absolute;background:var(--white);border:1px solid #cfcfcf;font-size:10px;color:#777;padding:7px 10px}
.submit{left:654px;top:3728px;width:79px;height:28px;font-size:11px}
.info-row{position:absolute;left:804px;display:flex;align-items:center;gap:22px;color:var(--white);font-size:11.5px;line-height:17px}
.info-icon{width:32px;height:32px;border-radius:50%;border:2px solid var(--white);display:flex;align-items:center;justify-content:center}
.socials{left:761px;top:3722px;display:flex;gap:8px}
.socials i{width:27px;height:27px;border-radius:50%;background:var(--blue)}
.socials i:nth-child(4){background:#b48a4e}
.foot-line{left:130px;top:3808px;width:940px;height:1px;background:#6a6a6c}
.copyright{left:0;width:1200px;top:3841px;text-align:center;font-size:11.5px;color:var(--white)}
</style>
</head>
<body>
<div class="page">

  <!-- hero -->
  <div class="abs hero-photo" role="img" aria-label="Businessman reading a document in front of a city skyline with a world map overlay"></div>
  <div class="abs hero-city" role="img" aria-label="City skyline"></div>
  <div class="abs hero-figure" role="img" aria-label="Businessman in a suit holding papers"></div>
  <svg class="abs" style="left:0;top:0" width="1200" height="790" viewBox="0 0 1200 790">
    <path d="M560,738 C800,742 1060,680 1200,540 L1200,790 L560,790Z" fill="var(--grey)"/>
    <path d="M0,540 C60,690 240,770 500,752 C640,742 780,728 900,712 L900,790 L0,790Z" fill="var(--blue)"/>
    <path d="M0,575 C80,720 300,782 600,768 C860,756 1060,760 1200,752 L1200,790 L0,790Z" fill="var(--white)"/>
  </svg>

  <header>
    <div class="abs logo"><span class="logo-dot"></span><span class="logo-name">TRELMOND</span></div>
    <nav class="abs nav">
      <span class="active">HOME</span><span>SERVICES</span><span>RISE</span><span>MERIT</span><span>RESOURCES</span><span>CONTACT</span>
    </nav>
  </header>

  <h1 class="abs heading hero-title"><span>Leading Organizations</span><span class="accent">To Excellence!</span></h1>
  <a class="btn" style="left:143px;top:388px;width:237px;height:64px;font-size:17px">Library Database</a>
  <div class="abs dots-v"><i></i><i></i><i class="on"></i><i></i></div>

  <!-- about -->
  <div class="abs about-photo" role="img" aria-label="Scientist examining a test sample in a laboratory"></div>
  <h2 class="abs heading about-title"><span class="accent">About</span> Us</h2>
  <p class="abs about-text">Trelmond Group was created to help nonprofits and government contractors meet their basic funding requirements and adopt a Mission Aligned Data Driven mindset that promotes positive change in the lives of the people they serve. Our approach is not simply based off of theoretical business practices, but on practical solutions to real-life situations learned through more than twenty years of experience.</p>
  <a class="btn" style="left:621px;top:1110px;width:153px;height:54px">Read More</a>

  <!-- services -->
  <div class="abs card-wedge"></div>
  <div class="card card-left" role="img" aria-label="Hand writing consulting keywords on a board">
    <h3>Training &amp;<br>Consulting</h3>
  </div>
  <div class="card card-mid">
    <h3>Data Analytics</h3>
    <p>One the most important, and frequently neglected, areas of organizational management is the analysis of data to accurately identify community needs and track progress towards the successful fulfillment of the entity's purpose. Our goal is to ensure each of our customers is equipped</p>
    <a class="btn">Read More</a>
  </div>
  <div class="card card-right" role="img" aria-label="Professional video camera">
    <h3>Storytelling</h3>
  </div>
  <div class="abs arrows">
    <span><svg width="12" height="12" viewBox="0 0 12 12"><path d="M8,1 L3,6 L8,11" fill="none" stroke="#555" stroke-width="1.6"/></svg></span>
    <span><svg width="12" height="12" viewBox="0 0 12 12"><path d="M4,1 L9,6 L4,11" fill="none" stroke="#555" stroke-width="1.6"/></svg></span>
  </div>

  <!-- testimonials -->
  <div class="abs testi-bg" role="img" aria-label="Group of young people laughing together, faded"></div>
  <h2 class="abs heading testi-title"><span class="accent">Customer</span> Testimonials</h2>
  <svg class="abs quote" width="60" height="46" viewBox="0 0 60 46">
    <path d="M4,44 C2,26 8,8 24,2 L26,8 C17,13 15,20 16,24 L26,24 L26,44Z M34,44 C32,26 38,8 54,2 L56,8 C47,13 45,20 46,24 L56,24 L56,44Z" fill="var(--blue)"/>
  </svg>
  <p class="abs testi-text">“It was a training, but not your typical training. It leaves you with a new and different take on things. You will find yourself saying ‘Wow, I’ve never thought of it like that before’. You will be left with new and refreshing ideas and different ways to approach situations.”</p>
  <p class="abs testi-author">– Ridgeway County Senior Services</p>
  <div class="abs dots-h"><i></i><i></i><i class="on"></i><i></i></div>

  <!-- mission -->
  <div class="abs mission-blue"></div>
  <div class="abs mission-grey"></div>
  <h2 class="abs heading mission-title">Our Mission</h2>
  <p class="abs mission-text">To help social service organizations develop a Mission Aligned Data Driven mindset that promotes positive change in the lives of the customers they serve.</p>

  <!-- team -->
  <div class="member" style="left:138px">
    <div class="member-ring">
      <svg class="abs" style="left:0;top:0" width="320" height="320" viewBox="0 0 320 320"><path d="M60,30 C150,-20 290,20 305,140 C312,200 290,250 250,275 C285,230 295,170 280,120 C255,50 160,10 60,30Z" fill="var(--blue)"/></svg>
      <div class="member-photo" style="background:linear-gradient(180deg,#8c8f84,#3a4556)" role="img" aria-label="Portrait of the CEO in a suit and tie"></div>
    </div>
    <h4>Daniel “Dane” Trelmond</h4>
    <div class="role">OUR CEO</div>
    <p>At vero eos et accusamus et iusto odio dignissimos ducimus qui blanditiis praesentium voluptatueleniti atque corrupti quos dolores et quas molestiase xcepturi sint occaecati cupiditate non providents imilique sunt in culpa officia deserunt</p>
    <a class="btn">Read More</a>
  </div>
  <div class="member" style="left:641px">
    <div class="member-ring">
      <svg class="abs" style="left:0;top:0" width="320" height="320" viewBox="0 0 320 320"><path d="M60,30 C150,-20 290,20 305,140 C312,200 290,250 250,275 C285,230 295,170 280,120 C255,50 160,10 60,30Z" fill="var(--blue)"/></svg>
      <div class="member-photo" style="background:linear-gradient(180deg,#5a4a42,#7a6250)" role="img" aria-label="Portrait of the CFO smiling"></div>
    </div>
    <h4>Marissa Colby Trelmond</h4>
    <div class="role">OUR CFO</div>
    <p>At vero eos et accusamus et iusto odio dignissimos ducimus qui blanditiis praesentium voluptatueleniti atque corrupti quos dolores et quas molestiase xcepturi sint occaecati cupiditate non providents imilique sunt in culpa officia deserunt</p>
    <a class="btn">Read More</a>
  </div>

  <!-- contact -->
  <svg class="abs" style="left:0;top:3260px" width="1200" height="622" viewBox="0 0 1200 622">
    <path d="M0,250 C180,120 380,60 600,40 C800,22 980,40 1200,120 L1200,622 L0,622Z" fill="var(--grey)"/>
    <path d="M520,40 C700,0 900,-6 1060,30 C1120,44 1170,70 1200,90 L1200,140 C1120,90 1040,68 940,56 C800,40 660,34 520,40Z" fill="var(--blue)"/>
    <path d="M0,240 C220,170 460,110 700,80 C780,70 840,64 900,62" fill="none" stroke="var(--white)" stroke-width="4"/>
  </svg>
  <h2 class="abs heading contact-title">Contact <span class="accent">Us</span></h2>

  <div class="abs label" style="left:188px;top:3520px">Get In Touch:</div>
  <div class="field" style="left:191px;top:3562px;width:266px;height:28px">NAME :</div>
  <div class="field" style="left:467px;top:3562px;width:266px;height:28px">PHONE :</div>
  <div class="field" style="left:191px;top:3603px;width:542px;height:28px">EMAIL :</div>
  <div class="field" style="left:191px;top:3643px;width:542px;height:64px">MESSAGE :</div>
  <a class="btn submit">Submit</a>

  <div class="abs label" style="left:804px;top:3520px">Contact Information</div>
  <div class="info-row" style="top:3562px">
    <span class="info-icon"><svg width="12" height="16" viewBox="0 0 12 16"><path d="M6,15 C2,10 1,8 1,6 A5,5 0 0 1 11,6 C11,8 10,10 6,15Z" fill="none" stroke="#fff" stroke-width="1.5"/><circle cx="6" cy="6" r="1.8" fill="#fff"/></svg></span>
    <span>4180 Larchmere Court<br>Dalton, Georgia 30721</span>
  </div>
  <div class="info-row" style="top:3609px">
    <span class="info-icon"><svg width="14" height="14" viewBox="0 0 14 14"><path d="M3,1 L5,4 L4,6 C5,8 6,9 8,10 L10,9 L13,11 L11,13 C6,13 1,8 1,3Z" fill="#fff"/></svg></span>
    <span>Phone : +1 (555) 014-2287</span>
  </div>
  <div class="info-row" style="top:3654px">
    <span class="info-icon"><svg width="14" height="10" viewBox="0 0 14 10"><rect x="0.5" y="0.5" width="13" height="9" fill="#fff"/><path d="M1,1 L7,6 L13,1" fill="none" stroke="var(--grey)" stroke-width="1.2"/></svg></span>
    <span>Email : info@trelmondgroup.com</span>
  </div>
  <div class="abs socials"><i></i><i></i><i></i><i></i><i></i></div>

  <div class="abs foot-line"></div>
  <p class="abs copyright">Copyrights © 2022, Trelmond Group. All Rights Reserved.&nbsp; | &nbsp;Privacy policy</p>

</div>
</body>
</html>
```